Facebook,Twitter and Google+ Page Design for a Babysitting Online Platform

I need to launch my Social Media presence on Facebook,Twitter and Google+ and therefore need Social Media Design for the 3 platforms mentioned above. I am providing a Online Babysitting Platform that will help Mothers find babysitters for their kids. The theme is trust, community feel and mother/kid relation.
Its called Tots Nest Aid.
The blue green and orange colour is the official logo.Please see attached.
Tag Line - "Get Babysitting Help from people you trust"

Please note the Tag Line is essentially a Call to Action and therefore needs to really stand out on the cover page
Updates

Dear Designers, Please note, i do not need a logo. I am startup and would like to establish a Facebook, Twitter and Google+ Page for my startup. I therefore need cover photo for these Social Media Sites . I have provided you with the logo. I am looking for something simple and not too complicated. Heres an example of a Facebook, Twitter and Google+ page for a startup called Class Finder: https://www.examplebook.test/ClassFinder https://chirpsite.test/ClassFinder https://circles.example.test/u/0/284019573610482957301/videos Thanks in advance Regards Mel

Reason: In order to ensure the best designers who maybe busy with other projects are able to apply. I am looking for something simple so please do apply

Target Market(s)

Target Customers - Mothers/Females
Colours should signify Trust, Love,Loyalty and more for women

Industry/Entity Type

Babysitting

Requirements
Must have
• Get Babysitting Help from the People you Trust is a Call to Action and has to be on the cover page
Nice to have
• Use just one simple colour and if possible have a nice clean image of Mother and Kids to show the love, compassion,trust
Should not have
• Too Many Colours, Images , Use of the Logo provided

```html
<!DOCTYPE html>
<html lang="en">
<head>
<meta charset="utf-8">
<title>Tots Nest Aid – Cover</title>
<link rel="stylesheet" href="https://fonts.googleapis.com/css2?family=Open+Sans:wght@600;700&display=swap">
<style>
  :root {
    --green-deep: #4c6e22;
    --green-mid: #7db346;
    --cream: #fbf7a6;
    --teal: #0fa39a;
    --sky: #1aa0e0;
    --orange: #f4a233;
    --gold-light: #fbe7b0;
    --gold: #e2b064;
    --tagline: #4a6a26;
    --brand: #4aa6b4;
    --white: #ffffff;
  }
  html, body {
    margin: 0;
    padding: 0;
    overflow: hidden;
    background: var(--white);
  }
  .cover {
    position: relative;
    width: 1200px;
    height: 676px;
    overflow: hidden;
    background: var(--white);
    font-family: "Open Sans", Arial, sans-serif;
  }
  .band-top {
    position: absolute;
    left: 0; top: 0;
    width: 1200px; height: 203px;
    background: linear-gradient(90deg,
      var(--green-deep) 0%,
      var(--green-mid) 30%,
      var(--cream) 52%,
      var(--green-mid) 74%,
      var(--green-deep) 100%);
  }
  .tagline {
    position: absolute;
    left: 455px; top: 148px;
    margin: 0;
    font-size: 24px;
    font-weight: 700;
    color: var(--tagline);
    white-space: nowrap;
  }
  .band-bottom {
    position: absolute;
    left: 0; top: 448px;
    width: 1200px; height: 228px;
    background: linear-gradient(90deg,
      var(--teal) 0%,
      var(--sky) 14%,
      var(--orange) 38%,
      var(--cream) 52%,
      var(--orange) 63%,
      var(--sky) 88%,
      var(--teal) 100%);
  }
  .rosette {
    position: absolute;
    border-radius: 50%;
    background: radial-gradient(circle, var(--white) 38%, var(--gold-light) 55%, var(--gold) 100%);
    opacity: 0.85;
  }
  .rosette-left {
    left: 28px; top: 155px;
    width: 334px; height: 334px;
  }
  .rosette-right {
    left: 922px; top: 219px;
    width: 234px; height: 234px;
  }
  .brand {
    position: absolute;
    left: 445px; top: 250px;
    display: flex;
    align-items: center;
    gap: 30px;
  }
  .brand-dot {
    width: 150px; height: 150px;
  }
  .brand-name {
    margin: 0;
    font-size: 72px;
    font-weight: 600;
    color: var(--brand);
    letter-spacing: -1px;
    white-space: nowrap;
  }
</style>
</head>
<body>
  <main class="cover">
    <div class="band-top"></div>
    <p class="tagline">Get Babysitting Help from people you trust</p>
    <div class="band-bottom"></div>

    <div class="rosette rosette-left" role="img" aria-label="Decorative golden interlaced ring rosette"></div>
    <div class="rosette rosette-right" role="img" aria-label="Decorative golden interlaced ring rosette"></div>

    <div class="brand">
      <svg class="brand-dot" viewBox="0 0 150 150" aria-hidden="true">
        <circle cx="75" cy="75" r="70" fill="#7db346"/>
      </svg>
      <h1 class="brand-name">Tots Nest Aid</h1>
    </div>
  </main>
</body>
</html>
```